social interest sharing site needs a web site design

we need a web site design for a social web platform.
the site is one page(main page), that is split into 3 sections
each section is a different color(red,green and blue)
and a user can choose to share each of the sections.
any section/color will contain boxes , each box can contain different media types.

the media types:
* list of URLS
* list of articles including title + image + description
* list of videos
* thumbnails of images
* calender
* list of emails

the main content will look like corkboardly layout
multiple boxes each box can contain different type of content as described above

each color is a different tab
each tab will have layout like corkboardly
Updates

please read the last description update.
and i uploaded an image that can explain the requirements better

thanks
Oren
 

Industry/Entity Type

Media

```html
<!DOCTYPE html>
<html lang="en">
<head>
<meta charset="utf-8">
<title>tricolio</title>
<link rel="stylesheet" href="https://fonts.googleapis.com/css2?family=Open+Sans:wght@300;400;600&family=PT+Serif&display=swap">
<style>
:root{
  --ink:#1b1b1b;
  --red:#fe7772; --red-deep:#7b2f2f; --red-soft:#b05e52;
  --green:#4fdfc0; --green-deep:#2e7c64; --green-soft:#4aae90;
  --blue:#465f8c; --blue-deep:#2d4a7b; --blue-soft:#5176b0;
  --arrow-bg:#2a2325; --label:#dadada;
}
*{box-sizing:border-box;margin:0;padding:0}
html,body{width:1024px;height:1200px;overflow:hidden;background:#fff}
.page{width:1200px;height:1406px;transform:scale(.85333);transform-origin:0 0;position:relative;font-family:"Open Sans",sans-serif;color:#fff}
.topbar{height:52px;background:var(--ink);position:relative}
.brand{position:absolute;left:140px;top:8px;font-size:23px;font-weight:400;letter-spacing:.2px;line-height:30px}
.nav{position:absolute;right:152px;top:17px;display:flex;gap:46px;font-size:13px}
.section{position:absolute;top:53px;width:300px}
.s1{left:130px}.s2{left:450px}.s3{left:770px}
.tab-icon{width:30px;height:27px;display:flex;align-items:center;justify-content:center}
.section-title{font-weight:300;font-size:32px;color:var(--label);margin:8px 0 6px 10px;height:41px;line-height:41px}
.column{padding:0 10px 10px}
.s1 .column{background:var(--red)}.s2 .column{background:var(--green)}.s3 .column{background:var(--blue)}
.card-title{font-family:"PT Serif",serif;font-weight:400;font-size:29px;line-height:33px;height:80px;padding:12px 8px 0}
.media{height:140px;position:relative;overflow:hidden}
.meta-row{height:70px;display:flex}
.meta{flex:1;font-size:12px;padding:6px 6px 0;line-height:21px}
.s1 .meta{background:var(--red-deep)}.s2 .meta{background:var(--green-deep)}.s3 .meta{background:var(--blue-deep)}
.meta svg{width:10px;height:10px;vertical-align:-1px;margin-right:6px}
.meta .likes b{font-weight:400;margin-left:16px}
.go{width:70px;background:var(--arrow-bg);display:flex;align-items:center;justify-content:center}
.photo{width:100%;height:100%;background:radial-gradient(circle at 45% 40%,#8a6a45,#3a2a18 60%,#1e170e)}
.photo.bright{background:radial-gradient(circle at 40% 45%,#6b5a4a,#2a2420 65%)}
.video{width:100%;height:100%;background:linear-gradient(160deg,#5a3a1c,#c07a2a 35%,#3a2210 60%,#d89a40 85%,#4a2a10)}
.play{position:absolute;left:50%;top:50%;transform:translate(-50%,-50%)}
.thumbs{display:grid;grid-template-columns:repeat(4,70px);grid-template-rows:repeat(2,70px);height:140px}
.thumbs i{display:block}
.blurb{display:flex;height:140px}
.blurb .text{font-size:11px;line-height:14.5px;padding:6px 6px}
.s1 .blurb .text{background:var(--red-soft)}.s2 .blurb .text{background:var(--green-soft)}
.calendar{display:flex;height:140px}
.calendar .text{width:84px;font-size:11px;line-height:14.5px;padding:6px 6px}
.s1 .calendar .text{background:var(--red-soft)}.s2 .calendar .text{background:var(--green-soft)}
.calendar table{border-collapse:collapse;background:#fff;color:#222;font-size:10px;width:196px;height:140px}
.calendar td{width:28px;height:28px;text-align:center;border:1px solid #e6e6e6}
.calendar td.wk{background:#f0f0f0}
.calendar td.today{background:#cfe4f7}
.list{height:140px;font-size:11px;padding:6px 7px;display:flex;flex-direction:column;justify-content:space-between;list-style:none}
.s1 .list{background:var(--red-soft)}.s3 .list{background:var(--blue-soft)}
.list svg{width:11px;height:8px;margin-right:6px;vertical-align:0}
.footer{position:absolute;top:1326px;left:0;width:1200px;height:46px;background:var(--ink);font-size:9px;letter-spacing:3px}
.footer .brand-small{position:absolute;left:139px;top:13px;font-size:13px;letter-spacing:0}
.legal{position:absolute;left:276px;top:19px;color:#bbb}
.f-links{position:absolute;right:140px;top:18px;display:flex;gap:56px;color:#bbb}
.hidden{position:absolute;width:0;height:0}
</style>
</head>
<body>
<svg class="hidden" aria-hidden="true">
  <symbol id="eye" viewBox="0 0 20 12"><path d="M1 6C4 1 16 1 19 6C16 11 4 11 1 6Z" fill="none" stroke="currentColor" stroke-width="1.8"/><circle cx="10" cy="6" r="2.6" fill="currentColor"/></symbol>
  <symbol id="thumb" viewBox="0 0 10 10"><rect x="0" y="4" width="2.5" height="6" fill="currentColor"/><path d="M3.2 4L5.5 0.5C6.5 0.5 6.8 1.5 6.3 3.5H9.4C10 3.5 10 4.5 9.6 5L8.4 9.6C8.2 10 8 10 7.6 10H3.2Z" fill="currentColor"/></symbol>
  <symbol id="mail" viewBox="0 0 11 8"><rect width="11" height="8" fill="currentColor"/><path d="M0 0L5.5 4.5L11 0" fill="none" stroke="#b05e52" stroke-width="1"/></symbol>
  <symbol id="chev" viewBox="0 0 24 34"><path d="M4 3L18 17L4 31" fill="none" stroke="#fff" stroke-width="5.5"/></symbol>
  <symbol id="playbtn" viewBox="0 0 60 60"><circle cx="30" cy="30" r="30" fill="#fff" fill-opacity=".45"/><path d="M22 15L46 30L22 45Z" fill="#555" fill-opacity=".85"/></symbol>
</svg>

<div class="page">
  <header class="topbar">
    <div class="brand">tricolio</div>
    <nav class="nav"><span>Lorem</span><span>Ipsum</span><span>Dolor</span><span>Login</span></nav>
  </header>

  <section class="section s1">
    <div class="tab-icon" style="background:var(--red)"><svg width="16" height="10" style="color:#fff"><use href="#eye"/></svg></div>
    <h2 class="section-title">Section 1</h2>
    <div class="column">
      <article class="card">
        <h3 class="card-title">Lorem ipsum dolor sumet</h3>
        <div class="media calendar">
          <div class="text">Duis eu iaculis quam. Proin ut vehicula ligula. Vesti-bulum eleifend ut dui non</div>
          <table><tr><td class="wk"></td><td>1</td><td>2</td><td>3</td><td class="today">4</td><td>5</td><td>6</td></tr><tr><td class="wk">7</td><td>8</td><td>9</td><td>10</td><td>11</td><td>12</td><td>13</td></tr><tr><td class="wk">14</td><td>15</td><td>16</td><td>17</td><td>18</td><td>19</td><td>20</td></tr><tr><td class="wk">21</td><td>22</td><td>23</td><td>24</td><td>25</td><td>26</td><td>27</td></tr><tr><td class="wk">28</td><td>29</td><td>30</td><td>31</td><td></td><td></td><td></td></tr></table>
        </div>
        <div class="meta-row"><div class="meta">22/10/2013<br><span class="likes"><svg><use href="#thumb"/></svg><b>2345</b></span><br><svg><use href="#eye"/></svg>123456</div><div class="go"><svg width="24" height="34"><use href="#chev"/></svg></div></div>
      </article>
      <article class="card">
        <h3 class="card-title">Lorem ipsum dolor sumet</h3>
        <div class="media"><div class="photo" role="img" aria-label="Portrait photograph of a woman on a warm dark background"></div></div>
        <div class="meta-row"><div class="meta">22/10/2013<br><span class="likes"><svg><use href="#thumb"/></svg><b>2345</b></span><br><svg><use href="#eye"/></svg>123456</div><div class="go"><svg width="24" height="34"><use href="#chev"/></svg></div></div>
      </article>
      <article class="card">
        <h3 class="card-title">Lorem ipsum dolor sumet</h3>
        <div class="media"><div class="video" role="img" aria-label="Video still: close-up of guitar strings"></div><svg class="play" width="60" height="60"><use href="#playbtn"/></svg></div>
        <div class="meta-row"><div class="meta">22/10/2013<br><span class="likes"><svg><use href="#thumb"/></svg><b>2345</b></span><br><svg><use href="#eye"/></svg>123456</div><div class="go"><svg width="24" height="34"><use href="#chev"/></svg></div></div>
      </article>
      <article class="card">
        <h3 class="card-title">Lorem ipsum dolor sumet</h3>
        <ul class="media list">
          <li><svg><use href="#mail"/></svg>brightlane@co.uk</li>
          <li><svg><use href="#mail"/></svg>loremipsum@fennelo.com</li>
          <li><svg><use href="#mail"/></svg>ipsumloremdolor@.co.uk</li>
          <li><svg><use href="#mail"/></svg>loremipsum@fennelo.com</li>
          <li><svg><use href="#mail"/></svg>ipsumloremdolor@.co.uk</li>
        </ul>
        <div class="meta-row"><div class="meta">22/10/2013<br><span class="likes"><svg><use href="#thumb"/></svg><b>2345</b></span><br><svg><use href="#eye"/></svg>123456</div><div class="go"><svg width="24" height="34"><use href="#chev"/></svg></div></div>
      </article>
    </div>
  </section>

  <section class="section s2">
    <div class="tab-icon" style="background:var(--green)"><svg width="16" height="10" style="color:#fff"><use href="#eye"/></svg></div>
    <h2 class="section-title">Section 2</h2>
    <div class="column">
      <article class="card">
        <h3 class="card-title">Lorem ipsum dolor sumet</h3>
        <div class="media thumbs" role="img" aria-label="Grid of eight image thumbnails">
          <i style="background:#7a8a5a"></i><i style="background:#3a5a9a"></i><i style="background:#d84a9a"></i><i style="background:#b89a4a"></i>
          <i style="background:#8ac05a"></i><i style="background:#e8a040"></i><i style="background:#4a6a8a"></i><i style="background:#7ab0d0"></i>
        </div>
        <div class="meta-row"><div class="meta">22/10/2013<br><span class="likes"><svg><use href="#thumb"/></svg><b>2345</b></span><br><svg><use href="#eye"/></svg>123456</div><div class="go"><svg width="24" height="34"><use href="#chev"/></svg></div></div>
      </article>
      <article class="card">
        <h3 class="card-title">Lorem ipsum dolor sumet</h3>
        <div class="media blurb">
          <div class="photo bright" style="width:140px;flex:none" role="img" aria-label="Article photograph of a laughing woman"></div>
          <div class="text">Duis eu iaculis quam. Proin ut vehicula ligula. Vestibulum eleifend ut dui non placerat. Vestibulum at erat id est rhoncus vestibulum.</div>
        </div>
        <div class="meta-row"><div class="meta">22/10/2013<br><span class="likes"><svg><use href="#thumb"/></svg><b>2345</b></span><br><svg><use href="#eye"/></svg>123456</div><div class="go"><svg width="24" height="34"><use href="#chev"/></svg></div></div>
      </article>
      <article class="card">
        <h3 class="card-title">Lorem ipsum dolor sumet</h3>
        <div class="media"><div class="photo" role="img" aria-label="Portrait photograph of a woman on a warm dark background"></div></div>
        <div class="meta-row"><div class="meta">22/10/2013<br><span class="likes"><svg><use href="#thumb"/></svg><b>2345</b></span><br><svg><use href="#eye"/></svg>123456</div><div class="go"><svg width="24" height="34"><use href="#chev"/></svg></div></div>
      </article>
      <article class="card">
        <h3 class="card-title">Lorem ipsum dolor sumet</h3>
        <div class="media calendar">
          <div class="text">Duis eu iaculis quam. Proin ut vehicula ligula. Vesti-bulum eleifend ut dui non</div>
          <table><tr><td class="wk"></td><td>1</td><td>2</td><td>3</td><td class="today">4</td><td>5</td><td>6</td></tr><tr><td class="wk">7</td><td>8</td><td>9</td><td>10</td><td>11</td><td>12</td><td>13</td></tr><tr><td class="wk">14</td><td>15</td><td>16</td><td>17</td><td>18</td><td>19</td><td>20</td></tr><tr><td class="wk">21</td><td>22</td><td>23</td><td>24</td><td>25</td><td>26</td><td>27</td></tr><tr><td class="wk">28</td><td>29</td><td>30</td><td>31</td><td></td><td></td><td></td></tr></table>
        </div>
        <div class="meta-row"><div class="meta">22/10/2013<br><span class="likes"><svg><use href="#thumb"/></svg><b>2345</b></span><br><svg><use href="#eye"/></svg>123456</div><div class="go"><svg width="24" height="34"><use href="#chev"/></svg></div></div>
      </article>
    </div>
  </section>

  <section class="section s3">
    <div class="tab-icon" style="background:var(--blue)"><svg width="16" height="10" style="color:#fff"><use href="#eye"/></svg></div>
    <h2 class="section-title">Section 3</h2>
    <div class="column">
      <article class="card">
        <h3 class="card-title">Lorem ipsum dolor sumet</h3>
        <div class="media"><div class="photo" role="img" aria-label="Portrait photograph of a woman on a warm dark background"></div></div>
        <div class="meta-row"><div class="meta">22/10/2013<br><span class="likes"><svg><use href="#thumb"/></svg><b>2345</b></span><br><svg><use href="#eye"/></svg>123456</div><div class="go"><svg width="24" height="34"><use href="#chev"/></svg></div></div>
      </article>
      <article class="card">
        <h3 class="card-title">Lorem ipsum dolor sumet</h3>
        <ul class="media list">
          <li>http://www.brightlane.co.uk/</li>
          <li>http://fennelo.com/</li>
          <li>http://www.brightlane.co.uk/</li>
          <li>http://fennelo.com/</li>
          <li>http://www.brightlane.co.uk/</li>
        </ul>
        <div class="meta-row"><div class="meta">22/10/2013<br><span class="likes"><svg><use href="#thumb"/></svg><b>2345</b></span><br><svg><use href="#eye"/></svg>123456</div><div class="go"><svg width="24" height="34"><use href="#chev"/></svg></div></div>
      </article>
      <article class="card">
        <h3 class="card-title">Lorem ipsum dolor sumet</h3>
        <div class="media thumbs" role="img" aria-label="Grid of eight image thumbnails">
          <i style="background:#7a8a5a"></i><i style="background:#3a5a9a"></i><i style="background:#d84a9a"></i><i style="background:#b89a4a"></i>
          <i style="background:#8ac05a"></i><i style="background:#e8a040"></i><i style="background:#4a6a8a"></i><i style="background:#7ab0d0"></i>
        </div>
        <div class="meta-row"><div class="meta">22/10/2013<br><span class="likes"><svg><use href="#thumb"/></svg><b>2345</b></span><br><svg><use href="#eye"/></svg>123456</div><div class="go"><svg width="24" height="34"><use href="#chev"/></svg></div></div>
      </article>
      <article class="card">
        <h3 class="card-title">Lorem ipsum dolor sumet</h3>
        <div class="media"><div class="video" role="img" aria-label="Video still: close-up of guitar strings"></div><svg class="play" width="60" height="60"><use href="#playbtn"/></svg></div>
        <div class="meta-row"><div class="meta">22/10/2013<br><span class="likes"><svg><use href="#thumb"/></svg><b>2345</b></span><br><svg><use href="#eye"/></svg>123456</div><div class="go"><svg width="24" height="34"><use href="#chev"/></svg></div></div>
      </article>
    </div>
  </section>

  <footer class="footer">
    <div class="brand-small">tricolio</div>
    <div class="legal">©2013 NORTHWIND KITES, INC. ALL RIGHTS RESERVED</div>
    <div class="f-links"><span>PRIVACY POLICY</span><span>TERMS AND CONDITIONS</span></div>
  </footer>
</div>
</body>
</html>
```